Willow Crest Beauty - Package Design

New Beauty label needing product packaging design. Looking for elegant and stylish design to represent our premium brand.

This project is for 1 label and 1 box design. The winning designer will be assigned another project for the next product in the range. (to be paid as a new project)

This product is for "Glacier Pearl Mask". Please see the label format and jar attached. Please note there are 2 different jars we are considering (will have a mud inside). Please feel free to choose whichever one suits your design best.

The labels and boxes are to retain the product information, such as size, ingredients etc, but is to be updated to our brand. You can move or display the other information as you wish.

the size of the glacier pearl mask color box is 72*72*85mm (length*width*height)
the size of glacier pearl mask label is 218*58mm (width*height)

Women 15 to 65

• Must be elegant and represent our brand which is a premium beauty product.
• Dark blue. Dark purple etc. Colours should compliment the logo

```html
<!DOCTYPE html>
<html lang="en">
<head>
<meta charset="utf-8">
<title>Willow Crest Beauty – Glacier Pearl Mask Labels</title>
<link rel="stylesheet" href="https://fonts.googleapis.com/css2?family=Oswald:wght@500&family=Open+Sans:wght@400;600&display=swap">
<style>
  :root {
    --backdrop: #e6e6e6;
    --label-dark: #211f20;
    --label-sheen: #5a5858;
    --teal: #4fa59c;
    --gold: #c9a24a;
    --silver: #b9b9b9;
    --ink-light: #e9e9e9;
    --mud-brown: #7a5424;
  }
  * { margin: 0; padding: 0; box-sizing: border-box; }
  html, body { width: 1200px; height: 832px; overflow: hidden; }
  body {
    background: var(--backdrop);
    font-family: "Open Sans", Arial, sans-serif;
    color: var(--ink-light);
    position: relative;
  }
  .label {
    position: absolute;
    left: 50px;
    width: 1100px;
    height: 292px;
    background: var(--label-dark);
    overflow: hidden;
    box-shadow: 0 6px 18px rgba(0,0,0,0.25);
  }
  .label--textured { top: 70px; background: linear-gradient(180deg, var(--label-sheen) 0%, #2c2a2b 40%, var(--label-dark) 70%, #141314 100%); }
  .label--plain { top: 450px; }
  .mud-band {
    position: absolute;
    left: 0; top: 84px;
    width: 880px; height: 56px;
    background: linear-gradient(90deg, rgba(122,84,36,0) 0%, rgba(122,84,36,0.9) 12%, var(--mud-brown) 50%, rgba(122,84,36,0.7) 85%, rgba(122,84,36,0) 100%);
    filter: blur(3px);
    border-radius: 50%;
  }
  .brand {
    position: absolute;
    left: 240px; top: 40px;
    display: flex; align-items: center; gap: 10px;
    font-weight: 600; font-size: 24px; color: var(--gold);
    letter-spacing: 0.5px;
  }
  .brand-dot { width: 12px; height: 12px; border-radius: 50%; background: var(--gold); }
  .product-title {
    position: absolute;
    left: 200px; top: 98px;
    font-family: "Oswald", "Arial Narrow", sans-serif;
    font-weight: 500; font-size: 46px; line-height: 1;
    color: var(--teal); text-transform: uppercase; letter-spacing: -1px;
    white-space: nowrap;
  }
  .product-benefits { position: absolute; left: 212px; top: 152px; font-size: 14px; white-space: nowrap; }
  .product-claim {
    position: absolute; left: 200px; top: 184px; width: 340px;
    font-size: 11.5px; line-height: 1.45; text-transform: uppercase; text-align: center;
  }
  .product-size { position: absolute; left: 320px; top: 228px; font-size: 12px; }
  .natural-badge {
    position: absolute; left: 104px; top: 154px;
    width: 72px; height: 72px; border-radius: 50%;
    background: radial-gradient(circle at 35% 30%, #f2f2f2, var(--silver) 55%, #777 100%);
  }
  .info { position: absolute; left: 620px; top: 34px; width: 460px; font-size: 11px; line-height: 1.35; }
  .info h2 { font-size: 15px; font-weight: 600; color: var(--teal); letter-spacing: 0.3px; margin-top: 10px; }
  .info h2:first-child { margin-top: 0; }
  .info .caution-text { font-size: 14px; letter-spacing: 0.3px; }
  .icons { position: absolute; left: 630px; top: 222px; display: flex; align-items: center; gap: 26px; }
  .icon-shape { width: 40px; height: 36px; border: 2px solid var(--ink-light); border-radius: 4px; }
  .icon-shape--round { border-radius: 50%; }
  .seal-dot { width: 38px; height: 38px; border-radius: 50%; background: #fff; margin-left: 18px; }
</style>
</head>
<body>

<section class="label label--textured">
  <div class="mud-band" role="img" aria-label="Brushed mud texture sweeping across the label"></div>
  <div class="brand"><span class="brand-dot"></span>Willow Crest Beauty</div>
  <h1 class="product-title">Glacier Pearl Mask</h1>
  <p class="product-benefits">Anti Acne . Deep Skin Cleanser . Pore Reducer</p>
  <p class="product-claim">100% natural mineral infused detoxifier packed<br>with vitamins to promote youthful skin</p>
  <p class="product-size">250g / 8.8 fl. oz</p>
  <div class="natural-badge"></div>
  <div class="info">
    <h2>INDICATIONS</h2>
    <p>Nature glacier pearl mask, 100% Natural &amp; Mineral-Rich Fromula, Absorts excess Oil and removes dead skin cells, Dirt and toxin revealin rediant and texture, Clarity and ton.</p>
    <h2>INGREDIENTS</h2>
    <p>Deionized Water, Pure Dead Se Mud, Kaolin, Shea Butter, Sunflower Oil, Aloe Vera Juice, Vegetable Glycerin, Jojoba Oil, Hickory Bark Extract, Calendula Oil, Xanthan Gum, Vitamin E, Hyaluraonic acid.</p>
    <h2>CAUTION</h2>
    <p class="caution-text">FOR EXTERNAL USE ONLY. Keep out of reach of children.</p>
  </div>
  <div class="icons">
    <div class="icon-shape"></div>
    <div class="icon-shape icon-shape--round"></div>
    <div class="seal-dot"></div>
  </div>
</section>

<section class="label label--plain">
  <div class="brand"><span class="brand-dot"></span>Willow Crest Beauty</div>
  <h1 class="product-title">Glacier Pearl Mask</h1>
  <p class="product-benefits">Anti Acne . Deep Skin Cleanser . Pore Reducer</p>
  <p class="product-claim">100% natural mineral infused detoxifier packed<br>with vitamins to promote youthful skin</p>
  <p class="product-size">250g / 8.8 fl. oz</p>
  <div class="natural-badge"></div>
  <div class="info">
    <h2>INDICATIONS</h2>
    <p>Nature glacier pearl mask, 100% Natural &amp; Mineral-Rich Fromula, Absorts excess Oil and removes dead skin cells, Dirt and toxin revealin rediant and texture, Clarity and ton.</p>
    <h2>INGREDIENTS</h2>
    <p>Deionized Water, Pure Dead Se Mud, Kaolin, Shea Butter, Sunflower Oil, Aloe Vera Juice, Vegetable Glycerin, Jojoba Oil, Hickory Bark Extract, Calendula Oil, Xanthan Gum, Vitamin E, Hyaluraonic acid.</p>
    <h2>CAUTION</h2>
    <p class="caution-text">FOR EXTERNAL USE ONLY. Keep out of reach of children.</p>
  </div>
  <div class="icons">
    <div class="icon-shape"></div>
    <div class="icon-shape icon-shape--round"></div>
    <div class="seal-dot"></div>
  </div>
</section>

</body>
</html>
```